Casas de Nueva Aurora Flyer

Make me a flyer postcard 5 x 7 horizontal, one sided. I want main title to be "Casas de Nueva Aurora". It needs to say “Familias que se forman en la fe y valores humanos, y trabajan para llevar a otras familias al encuentro con Cristo y la Virgen María.”  We are in 4 places, include this:
Reuniones Cada Domingo
Monte Tabor Alto, Falls Church: 11:15am - 301-555-0142
Luz Divina Norte, Sterling: 9:30am - 571-555-0187
Hogar Sol Naciente, 9:45am - 703-555-0129
Paz Eterna Sur, Winchester: 2:30pm - 540-555-0163
Include the logo attached, and use the picture attached as the main image, you can select the people from the image only and delete background or keep background but make it fit in nicely to the postcard.

```html
<!DOCTYPE html>
<html lang="es">
<head>
<meta charset="utf-8">
<title>Casas de Nueva Aurora – Flyer</title>
<link rel="stylesheet" href="https://fonts.googleapis.com/css2?family=Playfair+Display:wght@400;500;700;900&family=Alfa+Slab+One&family=Crimson+Text&display=swap">
<style>
:root{
  --backdrop:#cfcfcf;
  --rust-dark:#8e3f12;
  --rust-light:#b8661f;
  --paper:#ffffff;
  --wine:#5e0c0b;
  --wine-deep:#2a0605;
  --ink:#000000;
  --gold:#f6c86a;
  --gray-top:#5f5f5f;
  --gray-bottom:#a9a9a9;
  --panel:rgba(140,18,18,.55);
  --pin:#9b1b1b;
  --text-dark:#222;
}
*{margin:0;padding:0;box-sizing:border-box}
html,body{width:1200px;height:934px;overflow:hidden;background:var(--backdrop)}
.flyer{position:absolute;left:0;top:38px;width:1200px;height:857px;overflow:hidden;
  background:linear-gradient(180deg,var(--wine) 0%,var(--wine-deep) 70%,var(--ink) 100%)}
.band-top{position:absolute;left:0;top:0;width:1200px;height:165px;
  background:radial-gradient(ellipse at 30% 40%,var(--rust-light),var(--rust-dark) 80%)}
.band-white{position:absolute;left:0;top:165px;width:1200px;height:354px;background:var(--paper)}
.photo-art{position:absolute;left:0;top:0;width:1200px;height:519px}
.title-small{position:absolute;left:64px;top:52px;font-family:"Playfair Display",serif;font-weight:400;
  font-size:86px;line-height:1;color:var(--paper);letter-spacing:1px}
.title-big{position:absolute;left:62px;top:183px;font-family:"Playfair Display",serif;font-weight:900;
  font-size:110px;line-height:.98;letter-spacing:-1px;
  background:linear-gradient(180deg,var(--gray-top),var(--gray-bottom));
  -webkit-background-clip:text;background-clip:text;color:transparent}
.tagline{position:absolute;left:65px;top:420px;width:445px;font-family:"Crimson Text",serif;
  font-size:18.5px;line-height:25px;color:var(--text-dark)}
.meetings-head{position:absolute;left:65px;top:555px;width:1070px;display:flex;align-items:center;gap:14px}
.meetings-head .rule{flex:1;height:2px;background:var(--paper)}
.meetings-head h2{font-family:"Playfair Display",serif;font-weight:500;font-size:40px;color:var(--gold);white-space:nowrap}
.icon-art{position:absolute;left:63px;top:606px;width:132px;height:186px;
  clip-path:polygon(50% 0,100% 18%,100% 100%,0 100%,0 18%);
  background:linear-gradient(180deg,#a8823a,#6b4a1c)}
.icon-art::after{content:"";position:absolute;inset:10px;clip-path:polygon(50% 0,100% 17%,100% 100%,0 100%,0 17%);
  background:linear-gradient(160deg,#c8a14a 0%,#b02a1f 45%,#7a1410 100%)}
.schedule{position:absolute;left:215px;top:650px;width:918px;height:153px;border-radius:18px;
  background:var(--panel);display:grid;grid-template-columns:repeat(4,1fr);padding:20px 0}
.site{padding:0 8px 0 18px;border-left:1px solid rgba(255,255,255,.55);min-width:0}
.site:first-child{border-left:none}
.site-name{display:flex;gap:7px;font-family:"Alfa Slab One",serif;font-size:13.5px;line-height:17px;color:var(--gold);height:38px}
.site-name svg,.site-phone svg{flex:none;width:19px;height:19px;margin-top:1px}
.site-time{display:inline-block;margin-top:5px;padding:2px 12px;background:var(--paper);
  font-family:"Playfair Display",serif;font-weight:700;font-size:21px;line-height:27px;color:var(--ink);
  clip-path:polygon(6px 0,calc(100% - 6px) 0,100% 50%,calc(100% - 6px) 100%,6px 100%,0 50%)}
.site-phone{display:flex;align-items:center;gap:6px;margin-top:8px;font-family:"Alfa Slab One",serif;font-size:20px;color:var(--gold);white-space:nowrap}
</style>
</head>
<body>
<div class="flyer">
  <div class="band-top"></div>
  <div class="band-white"></div>

  <svg class="photo-art" viewBox="0 0 1200 519" role="img" aria-label="Foto de grupo de las familias de la comunidad al aire libre">
    <defs>
      <linearGradient id="scene" x1="0" y1="0" x2="0" y2="1">
        <stop offset="0" stop-color="#9cb9d8"/>
        <stop offset=".25" stop-color="#4d6a3c"/>
        <stop offset=".55" stop-color="#6e5a62"/>
        <stop offset=".8" stop-color="#b88750"/>
        <stop offset="1" stop-color="#a56b34"/>
      </linearGradient>
    </defs>
    <polygon points="862,0 1200,0 1200,114 880,114" fill="#fff"/>
    <polygon points="886,26 1200,26 1200,385 1094,519 462,519" fill="url(#scene)"/>
  </svg>

  <div class="title-small">CASAS DE</div>
  <div class="title-big">NUEVA<br>AURORA</div>
  <p class="tagline">Familias que se forman en la fe y valores humanos, y trabajan para llevar a otras familias al encuentro con Cristo y la Virgen María</p>

  <div class="meetings-head"><span class="rule"></span><h2>REUNIONES CADA DOMINGO</h2><span class="rule"></span></div>

  <div class="icon-art" role="img" aria-label="Icono religioso de la Sagrada Familia en marco dorado"></div>

  <div class="schedule">
    <div class="site">
      <div class="site-name"><svg viewBox="0 0 20 20"><circle cx="10" cy="10" r="10" fill="#fff"/><path d="M10 4a4 4 0 0 0-4 4c0 3 4 8 4 8s4-5 4-8a4 4 0 0 0-4-4zm0 5.5a1.5 1.5 0 1 1 0-3 1.5 1.5 0 0 1 0 3z" fill="#9b1b1b"/></svg><span>MONTE TABOR ALTO,<br>FALLS CHURCH</span></div>
      <span class="site-time">11:15AM</span>
      <div class="site-phone"><svg viewBox="0 0 20 20"><circle cx="10" cy="10" r="10" fill="#fff"/><path d="M7 5l2 2.5-1.2 1.3a7 7 0 0 0 3.4 3.4L12.5 11 15 13l-1 2c-4.5 0-9-4.5-9-9z" fill="#9b1b1b"/></svg>301-555-0142</div>
    </div>
    <div class="site">
      <div class="site-name"><svg viewBox="0 0 20 20"><circle cx="10" cy="10" r="10" fill="#fff"/><path d="M10 4a4 4 0 0 0-4 4c0 3 4 8 4 8s4-5 4-8a4 4 0 0 0-4-4zm0 5.5a1.5 1.5 0 1 1 0-3 1.5 1.5 0 0 1 0 3z" fill="#9b1b1b"/></svg><span>LUZ DIVINA NORTE,<br>STERLING</span></div>
      <span class="site-time">9:30AM</span>
      <div class="site-phone"><svg viewBox="0 0 20 20"><circle cx="10" cy="10" r="10" fill="#fff"/><path d="M7 5l2 2.5-1.2 1.3a7 7 0 0 0 3.4 3.4L12.5 11 15 13l-1 2c-4.5 0-9-4.5-9-9z" fill="#9b1b1b"/></svg>571-555-0187</div>
    </div>
    <div class="site">
      <div class="site-name"><svg viewBox="0 0 20 20"><circle cx="10" cy="10" r="10" fill="#fff"/><path d="M10 4a4 4 0 0 0-4 4c0 3 4 8 4 8s4-5 4-8a4 4 0 0 0-4-4zm0 5.5a1.5 1.5 0 1 1 0-3 1.5 1.5 0 0 1 0 3z" fill="#9b1b1b"/></svg><span>HOGAR SOL<br>NACIENTE</span></div>
      <span class="site-time">9:45AM</span>
      <div class="site-phone"><svg viewBox="0 0 20 20"><circle cx="10" cy="10" r="10" fill="#fff"/><path d="M7 5l2 2.5-1.2 1.3a7 7 0 0 0 3.4 3.4L12.5 11 15 13l-1 2c-4.5 0-9-4.5-9-9z" fill="#9b1b1b"/></svg>703-555-0129</div>
    </div>
    <div class="site">
      <div class="site-name"><svg viewBox="0 0 20 20"><circle cx="10" cy="10" r="10" fill="#fff"/><path d="M10 4a4 4 0 0 0-4 4c0 3 4 8 4 8s4-5 4-8a4 4 0 0 0-4-4zm0 5.5a1.5 1.5 0 1 1 0-3 1.5 1.5 0 0 1 0 3z" fill="#9b1b1b"/></svg><span>PAZ ETERNA SUR,<br>WINCHESTER</span></div>
      <span class="site-time">2:30PM</span>
      <div class="site-phone"><svg viewBox="0 0 20 20"><circle cx="10" cy="10" r="10" fill="#fff"/><path d="M7 5l2 2.5-1.2 1.3a7 7 0 0 0 3.4 3.4L12.5 11 15 13l-1 2c-4.5 0-9-4.5-9-9z" fill="#9b1b1b"/></svg>540-555-0163</div>
    </div>
  </div>
</div>
</body>
</html>
```